BSC Flyer to attract applicants 11x17

Brightline Stagecraft Company provides crew for local concerts, filming, theater, and corporate events.
The flyer will be posted on bulletin boards at colleges with theater programs.
Our primary venues are historic theaters in downtown LA
Need a 11x17 poster to attract potential applicants/crew
I have attached a poster that one of our staff made that has all if the relevant info - but i know the poster can look much better than that. I have also attached many images and our logo. It is not necessary to use all of the images, or any of them. The two images of the theater interiors are the venues we operate so they would be the first to include. I can send additional info or images upon request. Thank you

Entertainment

• APPLY@BSCCREWHUB.LA

```html
<!DOCTYPE html>
<html lang="en">
<head>
<meta charset="utf-8">
<title>Brightline Stagecraft Company – Open Positions</title>
<link href="https://fonts.googleapis.com/css2?family=Jost:ital,wght@0,400;0,500;0,600;1,400&family=Libre+Baskerville:wght@700&family=Arimo:wght@700&display=swap" rel="stylesheet">
<style>
  :root {
    --page: #ffffff;
    --paper: #e3e3e4;
    --brand-blue: #2559a8;
    --lavender: #9ea0d0;
    --texture-tone: #6d7097;
    --navy: #2f3653;
    --navy-deep: #353d5b;
    --white: #ffffff;
  }
  * { margin: 0; padding: 0; box-sizing: border-box; }
  html, body { width: 1200px; height: 1000px; overflow: hidden; background: var(--page); }
  .canvas { position: relative; width: 1200px; height: 1000px; }

  .poster {
    position: absolute; left: 298px; top: 38px; width: 605px; height: 925px;
    background: var(--paper); overflow: hidden;
    box-shadow: 0 6px 16px rgba(0,0,0,0.25);
  }

  .texture-patch {
    position: absolute; width: 46px; height: 46px; border-radius: 6px;
    background: linear-gradient(135deg, var(--texture-tone), var(--lavender));
    opacity: 0.75;
  }
  .texture-patch--top { left: 15px; top: 17px; }
  .texture-patch--mid { left: 537px; top: 517px; }

  .brand__disc {
    position: absolute; left: 115px; top: 52px; width: 110px; height: 110px;
    border-radius: 50%; background: var(--brand-blue);
  }
  .brand__name {
    position: absolute; left: 15px; top: 198px; width: 310px; text-align: center;
    font-family: "Jost", sans-serif; font-weight: 500; font-size: 24px;
    line-height: 27px; color: var(--brand-blue); letter-spacing: 0.3px;
  }

  .venue-frame {
    position: absolute; left: 318px; top: -130px; width: 440px; height: 440px;
    border-radius: 50%; background: var(--lavender);
  }
  .venue-frame__ring { position: absolute; inset: 10px; border-radius: 50%; background: var(--navy); }
  .venue-photo {
    position: absolute; inset: 5px; border-radius: 50%;
    background: radial-gradient(circle at 50% 70%, #e0a350 0%, #a4503f 30%, #5a2a5c 60%, #241a3a 100%);
  }

  .headline {
    position: absolute; left: 27px; top: 280px;
    font-family: "Libre Baskerville", serif; font-weight: 700; font-size: 54px;
    line-height: 70px; color: var(--brand-blue);
    text-shadow: 2px 3px 4px rgba(0,0,0,0.35);
  }

  .apply { position: absolute; left: 140px; top: 508px; width: 330px; text-align: center; color: var(--brand-blue); }
  .apply__label { font-family: "Jost", sans-serif; font-style: italic; font-size: 21px; line-height: 28px; }
  .apply__email { font-family: "Jost", sans-serif; font-weight: 600; font-size: 21px; line-height: 28px; letter-spacing: 0.4px; }

  .accent-band { position: absolute; left: 90px; top: 567px; width: 515px; height: 20px; background: var(--lavender); }

  .crowd-photo {
    position: absolute; left: 0; top: 587px; width: 605px; height: 282px;
    background: linear-gradient(180deg, #5a6285 0%, #454d70 45%, #2c3350 100%);
  }
  .accent-disc {
    position: absolute; left: -150px; top: 522px; width: 256px; height: 266px;
    border-radius: 50%; background: var(--lavender);
  }
  .pitch {
    position: absolute; left: 85px; top: 635px; width: 490px; text-align: center;
    font-family: "Arimo", sans-serif; font-weight: 700; font-size: 23px; line-height: 34px;
    color: var(--white);
  }

  .footer {
    position: absolute; left: 0; bottom: 0; width: 605px; height: 56px;
    background: var(--navy-deep); display: flex; align-items: center; justify-content: center;
  }
  .footer__url { font-family: "Jost", sans-serif; font-weight: 600; font-size: 21px; color: var(--white); letter-spacing: 1px; }
</style>
</head>
<body>
<div class="canvas">
  <main class="poster">
    <div class="texture-patch texture-patch--top" role="img" aria-label="Small decorative dot pattern"></div>

    <div class="brand__disc" aria-hidden="true"></div>
    <div class="brand__name">BRIGHTLINE STAGECRAFT<br>COMPANY</div>

    <div class="venue-frame">
      <div class="venue-frame__ring">
        <div class="venue-photo" role="img" aria-label="Ornate historic downtown theater interior with gilded proscenium stage and seating"></div>
      </div>
    </div>

    <h1 class="headline">HAS<br>OPEN<br>POSITIONS</h1>

    <div class="apply">
      <p class="apply__label">SEND RESUME TO</p>
      <p class="apply__email">APPLY@BSCCREWHUB.LA</p>
    </div>

    <div class="texture-patch texture-patch--mid" role="img" aria-label="Small decorative dot pattern"></div>

    <div class="accent-band" aria-hidden="true"></div>
    <div class="crowd-photo" role="img" aria-label="Concert crowd silhouetted with raised hands under stage lights"></div>
    <div class="accent-disc" aria-hidden="true"></div>

    <p class="pitch">we are looking for talented<br>technicians to add to our roster<br>of skilled professionals.</p>

    <footer class="footer">
      <span class="footer__url">WWW.BSCCREWHUB.LA</span>
    </footer>
  </main>
</div>
</body>
</html>
```